Informational Site for Advanced Chemistry R&D

The company develops oxidation chemistry for air, water, fuel pollution controls. The site has been prototyped at www.velkorlabs.net. Take a look. Now, the task is to design it for eye-catching beauty with use of color, on-page scroll-driven color transition and parallax effects. Should capture the themes: high technology, wow it's beautiful, modern, uncluttered, clean urban environment.

Target Market(s)

China Environmentally Conscious Government and Industry,

Industry/Entity Type

It Company

Number of Pages Required

3 page

Font styles to use
Sans Serif

Requirements
Must have
• Parallax effects, desktop compatible, Rich, Modern, Simple, Graphic
Nice to have
• Mobile Phone Compatible
Should not have
• Flash, or anything that is slow to load or requires high bandwidth

```html
<!DOCTYPE html>
<html lang="en">
<head>
<meta charset="utf-8">
<title>VelkorLabs — Oxidation Chemistry for Cleaner Air, Water and Fuel</title>
<link rel="stylesheet" href="https://fonts.googleapis.com/css2?family=Roboto:wght@400;500&family=Open+Sans:wght@400&display=swap">
<style>
  :root {
    --ink: #ffffff;
    --night: #050505;
    --bar: #1e1e1e;
    --sky-top: #1a1a1a;
    --sky-mid: #3a3a3a;
    --plant: #8a8a8a;
    --ground: #b9b9b9;
    --brand-blue: #1f74b8;
    --brand-teal: #2bb8bf;
    --logo-frame: #2a9fd0;
    --disc: rgba(0, 0, 0, 0.38);
  }
  * { box-sizing: border-box; margin: 0; padding: 0; }
  a { text-decoration: none; color: inherit; }
  html, body {
    width: 1200px; height: 895px; overflow: hidden;
    background: var(--night);
    font-family: "Roboto", Arial, sans-serif;
    color: var(--ink);
  }
  .page { position: relative; width: 1200px; height: 895px; overflow: hidden; }

  .hero { position: absolute; left: 0; top: 0; width: 1200px; height: 801px; }
  .hero-photo {
    position: absolute; inset: 0;
    background: linear-gradient(180deg, var(--sky-top) 0%, var(--sky-mid) 45%, var(--plant) 70%, var(--ground) 85%, #6f6f6f 100%);
  }
  .hero-disc {
    position: absolute; left: 282px; top: 149px; width: 600px; height: 600px;
    border-radius: 50%; background: var(--disc);
  }

  .nav-bar {
    position: absolute; left: 0; top: 31px; width: 1200px; height: 93px;
    background: var(--bar); opacity: 0.96;
  }
  .main-nav {
    position: absolute; top: 72px; right: 53px; height: 20px;
    display: flex; align-items: center; gap: 56px;
    list-style: none;
  }
  .main-nav a {
    color: var(--ink);
    font-size: 15px; font-weight: 400; letter-spacing: 0.1px;
  }

  .brand-box {
    position: absolute; left: 57px; top: 8px; width: 209px; height: 146px;
    background: #fff; border: 3px solid var(--logo-frame); border-radius: 2px;
    display: flex; flex-direction: column; align-items: center; justify-content: center; gap: 12px;
  }
  .brand-dot { width: 44px; height: 44px; border-radius: 50%; background: var(--brand-blue); }
  .brand-name { font-size: 25px; font-weight: 500; color: var(--brand-blue); }

  .hero-copy {
    position: absolute; left: 282px; top: 342px; width: 600px; text-align: center;
  }
  .hero-title { font-size: 57px; font-weight: 500; color: var(--brand-teal); line-height: 68px; letter-spacing: -0.5px; }
  .hero-text {
    width: 540px; margin: 23px auto 0;
    font-family: Arial, "Helvetica Neue", sans-serif;
    font-size: 15px; line-height: 23px;
  }
  .read-more {
    display: inline-block; margin-top: 27px; width: 133px; height: 38px; line-height: 36px;
    background: #000; border: 1px solid #fff; color: var(--ink);
    font-size: 13.5px;
  }

  .slide-arrow {
    position: absolute; top: 379px; width: 37px; height: 37px;
    border: 1.5px solid #fff; border-radius: 50%;
    display: flex; align-items: center; justify-content: center;
  }
  .slide-arrow.prev { left: 46px; }
  .slide-arrow.next { left: 1115px; }

  .site-footer {
    position: absolute; left: 0; top: 801px; width: 1200px; height: 94px; background: var(--night);
  }
  .copyright {
    position: absolute; left: 59px; top: 39px;
    font-family: "Open Sans", Arial, sans-serif; font-size: 12.5px; color: #e6e6e6;
  }
  .social { position: absolute; left: 1038px; top: 28px; display: flex; gap: 13px; list-style: none; }
  .social a {
    display: flex; align-items: center; justify-content: center;
    width: 30px; height: 30px; border: 1px solid #fff;
  }
  .social-dot { width: 10px; height: 10px; border-radius: 50%; background: #fff; }
</style>
</head>
<body>
<div class="page">
  <section class="hero">
    <div class="hero-photo" role="img" aria-label="Black and white photograph of an industrial power plant with chimneys, pipework and cooling units against a dark sky"></div>
    <div class="hero-disc"></div>

    <div class="nav-bar"></div>
    <ul class="main-nav">
      <li><a href="#">HOME</a></li>
      <li><a href="#">ABOUT US</a></li>
      <li><a href="#">TECHNOLOGY</a></li>
      <li><a href="#">PRODUCTS</a></li>
      <li><a href="#">CONTACT US</a></li>
    </ul>

    <a class="brand-box" href="#" aria-label="VelkorLabs home">
      <span class="brand-dot"></span>
      <span class="brand-name">VelkorLabs</span>
    </a>

    <div class="hero-copy">
      <h1 class="hero-title">VelkorLabs</h1>
      <p class="hero-text">Lorem ipsum dolor sit amet, consectetur adipiscing elit, sed do eiusmod tempor incididunt ut labore et dolore magna aliqua. Ut enim ad minim veniam, quis nostrud exercitation ullamco laboris</p>
      <a class="read-more" href="#">READ MORE</a>
    </div>

    <a class="slide-arrow prev" href="#" aria-label="Previous slide">
      <svg width="12" height="14" viewBox="0 0 12 14"><path d="M8 2 L3 7 L8 12" fill="none" stroke="#fff" stroke-width="2.4" stroke-linecap="round" stroke-linejoin="round"/></svg>
    </a>
    <a class="slide-arrow next" href="#" aria-label="Next slide">
      <svg width="12" height="14" viewBox="0 0 12 14"><path d="M4 2 L9 7 L4 12" fill="none" stroke="#fff" stroke-width="2.4" stroke-linecap="round" stroke-linejoin="round"/></svg>
    </a>
  </section>

  <footer class="site-footer">
    <p class="copyright">All Right Reserved. Copyright ©2016</p>
    <ul class="social">
      <li><a href="#" aria-label="Social profile one"><span class="social-dot"></span></a></li>
      <li><a href="#" aria-label="Social profile two"><span class="social-dot"></span></a></li>
      <li><a href="#" aria-label="Social profile three"><span class="social-dot"></span></a></li>
    </ul>
  </footer>
</div>
</body>
</html>
```